International Financial Organization needs a new Digital Workplace home page design

We need creative designs for the new Digital Workplace that will replace the current Intranet for an international organization based in Washington DC.

Organization Background: An organization of 189 countries, working to foster global monetary cooperation, secure financial stability, facilitate international trade, promote high employment and sustainable economic growth, and reduce poverty around the world.

Digital Workplace: The Digital workplace will be the central location that allows employees to do their work in productive, simple, and integrated manner.
Knowledge and Information are the lifeblood of our organization. Economists and experts conduct a lot of data-heavy research and produce a lot of reports and documents. The digital workplace will need to facilitate sharing of knowledge and collaboration among employees, and save them the hassle from going to multiple digital locations to do their work. Therefore the seamless integration of systems, and mobile-first design, is key.

Country Missions: A number of our economists travel on "missions" to countries all over the world on periodic basis to meet with country officials, present and discuss findings, and provide consultation. Before they go on missions, these economist do a lot of preparation and research about that country, and they collaborate in teams. When on mission (sometimes in areas that have very limited bandwidth connectivity) they need access to their documents, research, and resources and they need to collaborate with one another. Therefore mobility (velaphone, tabrik, laptop and desktops) and personalization are very important design criteria. When they are back from their mission they need to document reports and findings, and they will need to work on that through multiple systems.

Design Concept: We attach a concept of the digital workplace homepage (power point slides). The concept offers three views (the three tabs at the top: Enterprise View, Departmental View, and My View.)
The enterprise view is meant to be for all the users in the organization, and displays information that the org want to push to all employees. Not much of personalization is listed in this this view. We only provide the name of potential tiles there. Please be creative and think out of the box, we are open for ideas. The second view is the departmental view. It is meant to focus on the news, events, and information that the department want to share with me as an employee of that department. We only provide the name of potential tiles there. Please be creative and think out of the box, we are open for ideas.
Finally, “My View” is illustrated with sample tiles of what we envision to be used there. We provide two variations for our vision of the “My View”. The tiles that are listed there are not meant to be in that same exact location. Please feel free to change the groupings of these tiles as the page allows (We had to fit our design on 16:9 PPT slide so it’s a not a real page). Also, these tiles are not mean to be restrictive, please be creative and suggest other tiles as you’d envision a modern Digital Workplace. We are open for ideas!

Deliverables: we expect to see at least one creative design per each of these 3 views of the home page for desktop view, and the equivalent in mobile view. In addition we expect any other views/variations that your creativity inspires.

Preferred color pallet: blue, green, orange, and all their gradients. Also open for other colors as your creativity inspires for an established, very mature, and well-respected, international financial organization.

Thank you!

```html
<!DOCTYPE html>
<html lang="en">
<head>
<meta charset="utf-8">
<title>Hub Point – My View</title>
<link href="https://fonts.googleapis.com/css2?family=Bree+Serif&family=Merriweather:wght@400;700&family=Poppins:wght@400&family=Montserrat:wght@500&display=swap" rel="stylesheet">
<style>
:root{
  --cyan:#0bb6dc;
  --orange:#ff6b1f;
  --card:#f7f7f7;
  --ink:#444;
  --ink-soft:#666;
  --line:#e3e3e3;
  --link:#0a9fd0;
  --word:#2b5797;
  --excel:#3c8d3c;
  --pdf:#d23b2b;
  --teal:#5bc4cf;
  --red:#f04b4b;
  --yellow:#f9c623;
  --lime:#b5d56a;
  --pink:#d63c8a;
  --skin:#d9b49a;
}
*{margin:0;padding:0;box-sizing:border-box}
html,body{width:1200px;height:749px;overflow:hidden;background:#fff}
body{position:relative;font-family:'Merriweather',Georgia,serif;color:var(--ink);font-size:9px}
ul{list-style:none}
.abs{position:absolute}

/* header */
.brand{position:absolute;left:76px;top:6px;font-family:'Bree Serif',serif;font-size:21px;color:var(--orange)}
.view-tabs{position:absolute;left:77px;top:33px;display:flex;gap:18px;font-size:8.5px;color:var(--ink)}
.site-nav{position:absolute;left:584px;top:30px;display:flex;gap:24px;font-size:8.5px}
.greeting{position:absolute;right:112px;top:15px;font-family:'Bree Serif',serif;font-size:12.5px;color:#555;white-space:nowrap}
.greeting span{color:var(--orange)}
.user-photo{position:absolute;left:1093px;top:4px;width:44px;height:37px;background:linear-gradient(135deg,#c89a7c,#8a5a44)}

.bar{position:absolute;left:76px;background:var(--cyan);display:flex;align-items:center;justify-content:center;color:#fff;font-weight:700;font-size:8.6px}
.bar span{white-space:nowrap}
.main-nav{top:46px;width:1063px;height:29px}
.actions{top:300px;width:1065px;height:29px}

/* cards */
.card{position:absolute;background:var(--card)}
.card h3{position:absolute;font-weight:400;font-size:11px;color:#444;white-space:nowrap}
.rows{position:absolute;left:0;right:0}
.rows li{position:absolute;left:0;right:0;display:flex;align-items:center;height:14px;white-space:nowrap}
.rows li span{position:absolute}
.see-all{position:absolute;font-size:7.5px;color:var(--link);text-decoration:underline}

.doc-icon{width:15px;height:15px;border-radius:2px;display:inline-block}
.doc-icon.word{background:var(--word)}
.doc-icon.sheet{background:var(--excel)}
.doc-icon.pdf{background:#fff;border:1px solid #bbb;border-bottom:5px solid var(--pdf)}

.avatar{position:absolute;border-radius:50%;background:var(--skin)}
.avatar.dark{background:#6c5448}
.avatar.light{background:#e8cfa9}

.chat{position:absolute;font-family:'Poppins',sans-serif;font-size:7px;line-height:15px;color:#666;width:200px}
.reply-box{position:absolute;background:#ececec;width:220px;height:28px}
.post-btn{position:absolute;background:var(--orange);color:#fff;font-family:'Montserrat',sans-serif;font-size:7.5px;width:31px;height:12px;display:flex;align-items:center;justify-content:center}

.analytics{border:1px solid #777;background:#fff}

footer{position:absolute;left:0;top:705px;width:1200px;height:44px;background:var(--orange);color:#fff;font-family:'Montserrat',sans-serif;font-size:11px}
footer .copy{position:absolute;left:559px;top:14px}
footer .code{position:absolute;left:1119px;top:14px}
</style>
</head>
<body>

<header>
  <div class="brand">Hub Point</div>
  <nav class="view-tabs"><span>Enterprise Homepage</span><span>Dept. View</span><span>My View</span></nav>
  <nav class="site-nav"><span>Home</span><span>View</span><span>Contact Us</span></nav>
  <div class="greeting">Good Morning <span>Jane!</span></div>
  <div class="user-photo" role="img" aria-label="Profile photo of Jane"></div>
</header>

<nav class="bar main-nav">
  <span class="abs" style="left:203px">My HR</span>
  <span class="abs" style="left:296px">My Training</span>
  <span class="abs" style="left:416px">My Benefits</span>
  <span class="abs" style="left:533px">My Dependents</span>
  <span class="abs" style="left:663px">My Health Insurance</span>
  <span class="abs" style="left:817px">My Salary</span>
</nav>

<section class="card docs" style="left:76px;top:102px;width:247px;height:173px">
  <h3 style="left:17px;top:16px">My Recent Docs</h3>
  <ul class="rows">
    <li style="top:40px"><span style="left:17px" class="doc-icon word"></span><span style="left:37px">Document file name 1</span><span style="left:192px">10/0/2017</span></li>
    <li style="top:66px"><span style="left:17px" class="doc-icon sheet"></span><span style="left:37px">Spreadsheet file name 2</span><span style="left:192px">10/0/2017</span></li>
    <li style="top:92px"><span style="left:17px" class="doc-icon pdf"></span><span style="left:37px">PDF document file 3</span><span style="left:192px">10/0/2017</span></li>
    <li style="top:118px"><span style="left:17px" class="doc-icon word"></span><span style="left:37px">Document file name 1</span><span style="left:192px">10/0/2017</span></li>
    <li style="top:144px"><span style="left:17px" class="doc-icon sheet"></span><span style="left:37px">Spreadsheet file name 2</span><span style="left:192px">10/0/2017</span></li>
  </ul>
</section>

<section class="card email" style="left:343px;top:102px;width:299px;height:173px">
  <h3 style="left:18px;top:15px">My Recent Email</h3>
  <ul class="rows" style="font-size:8.3px">
    <li style="top:44px"><span style="left:18px">Lorem ipsum dolor sit amet...</span><span style="left:162px">Robert Thomas</span><span style="left:244px">9:23 am</span></li>
    <li style="top:67px"><span style="left:18px">Et donec ligula feugiat</span><span style="left:162px">Jane Arnold</span><span style="left:244px">8:30 am</span></li>
    <li style="top:90px"><span style="left:18px">Dapibus imperdiet vitae co...</span><span style="left:162px">James Marlow</span><span style="left:244px">8:22 am</span></li>
    <li style="top:113px"><span style="left:18px">Lorem ipsum dolor sit amet...</span><span style="left:162px">Robert Thomas</span><span style="left:244px">7:43 am</span></li>
    <li style="top:135px"><span style="left:18px">Duis vel eu velit, suspendisse</span><span style="left:162px">Jurgen Klaus</span><span style="left:244px">12:30 am</span></li>
  </ul>
</section>

<section class="card meetings" style="left:662px;top:102px;width:206px;height:173px">
  <h3 style="left:23px;top:15px">My Upcoming Meeting</h3>
  <ul class="rows" style="font-size:8.3px">
    <li style="top:44px"><span style="left:23px">Meeting 1</span><span style="left:85px">HQ2 7B-073</span><span style="left:160px">2:30pm</span></li>
    <li style="top:68px"><span style="left:23px">Meeting 2</span><span style="left:85px">HQ2 7B-073</span><span style="left:160px">2:30pm</span></li>
    <li style="top:92px"><span style="left:23px">Meeting 3</span><span style="left:88px">HQ2 7B-073</span><span style="left:160px">2:30pm</span></li>
    <li style="top:116px"><span style="left:23px">Meeting 4</span><span style="left:85px">HQ2 7B-073</span><span style="left:158px">2:30pm</span></li>
  </ul>
</section>

<section class="card tasks" style="left:886px;top:102px;width:256px;height:173px">
  <h3 style="left:15px;top:15px">My Tasks</h3>
  <ul class="rows" style="font-size:8px">
    <li style="top:44px"><span style="left:15px">Review Georgia's 2017 Article IV Report</span><span style="left:193px">01/06/2017</span></li>
    <li style="top:68px"><span style="left:15px">Submit Conference Selections</span><span style="left:193px">01/06/2017</span></li>
    <li style="top:92px"><span style="left:15px">Complete GFR chapter 2 data analysis</span><span style="left:193px">01/06/2017</span></li>
  </ul>
  <span class="see-all" style="left:213px;top:149px">See All</span>
</section>

<nav class="bar actions">
  <span class="abs" style="left:114px">Create New Document</span>
  <span class="abs" style="left:249px">Create New Spreadsheet</span>
  <span class="abs" style="left:392px">Create New Email message</span>
  <span class="abs" style="left:549px">Schedule a meeting</span>
  <span class="abs" style="left:676px">Create New Task</span>
  <span class="abs" style="left:787px">Book Travel</span>
  <span class="abs" style="left:878px">Submit Expenses</span>
</nav>

<section class="card conversations" style="left:76px;top:353px;width:275px;height:332px">
  <h3 style="left:29px;top:19px">My Recent Conversations</h3>
  <div class="avatar dark" style="left:20px;top:47px;width:24px;height:24px" role="img" aria-label="Colleague portrait"></div>
  <p class="chat" style="left:51px;top:46px">Lorem ipsum dolor sit amet, et donec ligula feugiat,<br>tempor quis consectetuer ipsum... <svg width="10" height="9" viewBox="0 0 10 9"><path d="M1 4h2v5H1zM3.5 4L5.5 0.5c1 0 1.3.8 1 2L6 4h3c.6 0 1 .5.8 1l-1 3.3c-.2.5-.5.7-1 .7H3.5z" fill="none" stroke="#2f8fd8" stroke-width=".9"/></svg></p>
  <div class="avatar light" style="left:39px;top:84px;width:24px;height:24px" role="img" aria-label="Colleague portrait"></div>
  <p class="chat" style="left:69px;top:83px">Lorem ipsum dolor sit amet, et donec ligula feugiat,<br>tempor quis consectetuer ipsum... <svg width="9" height="8" viewBox="0 0 10 9"><path d="M5 9L1 5C-.5 3.5.5.5 2.7.5 3.8.5 4.5 1.2 5 2c.5-.8 1.2-1.5 2.3-1.5C9.5.5 10.5 3.5 9 5z" fill="#e0262b"/></svg></p>
  <div class="reply-box" style="left:29px;top:128px"></div>
  <div class="post-btn" style="left:219px;top:158px">Post</div>

  <div class="avatar" style="left:20px;top:190px;width:24px;height:24px" role="img" aria-label="Colleague portrait"></div>
  <p class="chat" style="left:51px;top:189px">Lorem ipsum dolor sit amet, et donec ligula feugiat,<br>tempor quis consectetuer ipsum...</p>
  <div class="avatar" style="left:39px;top:227px;width:24px;height:24px" role="img" aria-label="Colleague portrait"></div>
  <p class="chat" style="left:69px;top:226px">Lorem ipsum dolor sit amet, et donec ligula feugiat,<br>tempor quis consectetuer ipsum... <svg width="10" height="9" viewBox="0 0 10 9"><path d="M1 4h2v5H1zM3.5 4L5.5 0.5c1 0 1.3.8 1 2L6 4h3c.6 0 1 .5.8 1l-1 3.3c-.2.5-.5.7-1 .7H3.5z" fill="none" stroke="#2f8fd8" stroke-width=".9"/></svg></p>
  <div class="reply-box" style="left:29px;top:269px"></div>
  <div class="post-btn" style="left:219px;top:300px">Post</div>
</section>

<section class="card teams" style="left:378px;top:353px;width:234px;height:164px">
  <h3 style="left:37px;top:19px">My Teams/Communities</h3>
  <ul class="rows" style="font-size:8.3px">
    <li style="top:47px"><span style="left:37px">Bulgaria - June 2017 Mission</span></li>
    <li style="top:75px"><span style="left:37px">Romania - April 2016 Mission</span></li>
    <li style="top:103px"><span style="left:37px">Bulgaria Country Team</span></li>
    <li style="top:131px"><span style="left:37px">Macedonia Country Team</span></li>
  </ul>
  <span class="see-all" style="left:190px;top:140px">See All</span>
</section>

<section class="card colleagues" style="left:378px;top:524px;width:234px;height:164px">
  <h3 style="left:35px;top:12px;font-size:10px">My Colleagues / Frequent Contacts</h3>
  <div class="avatar dark" style="left:37px;top:38px;width:25px;height:25px" role="img" aria-label="Portrait of Robert Thomas"></div>
  <div class="avatar" style="left:37px;top:69px;width:25px;height:25px" role="img" aria-label="Portrait of Chang Lee"></div>
  <div class="avatar light" style="left:37px;top:100px;width:25px;height:25px" role="img" aria-label="Portrait of Oswald Muhoza"></div>
  <div class="avatar" style="left:37px;top:132px;width:25px;height:25px" role="img" aria-label="Portrait of Jurgen Klaus"></div>
  <ul class="rows" style="font-size:8.3px">
    <li style="top:43px"><span style="left:71px">Robert Thomas, Mission Chief</span></li>
    <li style="top:74px"><span style="left:71px">Chang Lee, Senior Economist</span></li>
    <li style="top:105px"><span style="left:71px">Oswald Muhoza, Resident Rep</span></li>
    <li style="top:137px"><span style="left:71px">Jurgen Klaus, Desk Economist</span></li>
  </ul>
</section>

<section class="card news" style="left:642px;top:356px;width:499px;height:164px">
  <h3 style="left:42px;top:19px">My News Report</h3>
  <ul class="rows" style="font-size:8.3px">
    <li style="top:45px"><span style="left:42px">Banks' Preparations for Brexit Need to Improve - CEB, BoN (Newswire) 11:32 am</span><span style="left:381px">05/06/2017</span></li>
    <li style="top:73px"><span style="left:42px">Eurozone recovery broadening but gaps remain (GlobeWire)&nbsp; 9:03 am</span><span style="left:381px">05/06/2017</span></li>
    <li style="top:101px"><span style="left:42px">Lorem ipsum dolor sit amet, et donec ligula feugiat, tempor quis co... 5:45 pm</span><span style="left:381px">05/06/2017</span></li>
  </ul>
  <span class="see-all" style="left:449px;top:136px">See All</span>
</section>

<section class="card analytics" style="left:642px;top:532px;width:497px;height:151px">
  <h3 style="left:34px;top:12px">My Analytics</h3>
  <span class="abs" style="left:65px;top:42px;font-size:5.5px;color:#555">Average From Prior 30 period</span>
  <svg class="abs" style="left:30px;top:52px" width="155" height="78" viewBox="0 0 155 78">
    <g stroke="#eee" stroke-width=".6">
      <line x1="4" y1="6" x2="153" y2="6"/><line x1="4" y1="20" x2="153" y2="20"/><line x1="4" y1="34" x2="153" y2="34"/>
      <line x1="4" y1="48" x2="153" y2="48"/><line x1="4" y1="62" x2="153" y2="62"/><line x1="4" y1="72" x2="153" y2="72"/>
    </g>
    <g>
      <rect x="8" y="64" width="9" height="8" fill="var(--yellow)"/><rect x="8" y="58" width="9" height="6" fill="var(--red)"/><rect x="8" y="52" width="9" height="6" fill="var(--teal)"/>
      <rect x="23" y="54" width="9" height="18" fill="var(--yellow)"/><rect x="23" y="42" width="9" height="12" fill="var(--red)"/><rect x="23" y="22" width="9" height="20" fill="var(--teal)"/>
      <rect x="38" y="62" width="9" height="10" fill="var(--yellow)"/><rect x="38" y="54" width="9" height="8" fill="var(--red)"/><rect x="38" y="32" width="9" height="22" fill="var(--teal)"/>
      <rect x="53" y="52" width="9" height="20" fill="var(--yellow)"/><rect x="53" y="16" width="9" height="36" fill="var(--red)"/><rect x="53" y="8" width="9" height="8" fill="var(--teal)"/>
      <rect x="68" y="56" width="9" height="16" fill="var(--yellow)"/><rect x="68" y="30" width="9" height="26" fill="var(--red)"/><rect x="68" y="18" width="9" height="12" fill="var(--teal)"/>
      <rect x="83" y="66" width="9" height="6" fill="var(--yellow)"/><rect x="83" y="58" width="9" height="8" fill="var(--red)"/>
      <rect x="98" y="54" width="9" height="18" fill="var(--yellow)"/><rect x="98" y="46" width="9" height="8" fill="var(--red)"/><rect x="98" y="34" width="9" height="12" fill="var(--teal)"/>
      <rect x="113" y="52" width="9" height="20" fill="var(--yellow)"/><rect x="113" y="32" width="9" height="20" fill="var(--red)"/><rect x="113" y="10" width="9" height="22" fill="var(--teal)"/>
      <rect x="128" y="64" width="9" height="8" fill="var(--yellow)"/><rect x="128" y="56" width="9" height="8" fill="var(--red)"/><rect x="128" y="44" width="9" height="12" fill="var(--teal)"/>
    </g>
  </svg>
  <svg class="abs" style="left:206px;top:52px" width="76" height="76" viewBox="0 0 76 76">
    <g fill="none" stroke-width="6">
      <circle cx="38" cy="38" r="34" stroke="var(--lime)"/>
      <path d="M38 4A34 34 0 0 0 18 65.5" stroke="var(--teal)"/>
      <path d="M38 4A34 34 0 0 1 60 12" stroke="#2a9aa8"/>
    </g>
  </svg>
  <svg class="abs" style="left:300px;top:53px" width="150" height="76" viewBox="0 0 150 76">
    <g stroke="#eee" stroke-width=".6">
      <line x1="4" y1="6" x2="148" y2="6"/><line x1="4" y1="18" x2="148" y2="18"/><line x1="4" y1="30" x2="148" y2="30"/>
      <line x1="4" y1="42" x2="148" y2="42"/><line x1="4" y1="54" x2="148" y2="54"/><line x1="4" y1="66" x2="148" y2="66"/>
    </g>
    <polyline points="6,42 20,36 34,40 50,24 66,22 82,28 98,22 114,20 128,10 144,10" fill="none" stroke="var(--lime)" stroke-width="1"/>
    <polyline points="6,62 20,48 34,52 50,36 66,42 82,38 98,44 114,32 128,14 144,22" fill="none" stroke="var(--pink)" stroke-width="1"/>
  </svg>
</section>

<footer>
  <span class="copy">© 2017 Hub Point. All Rights Reserved.</span>
  <span class="code">C12</span>
</footer>

</body>
</html>
```